Supplement Label Redesign- Orla Menvik

We want to redesign this label to give it a fresh new look. Stay clean and contemporary similar to the designs on the JPEG. She likes the various blue and gray colors primarily but is open. The label should be professional for a doctor but still have some artistic expression.

The Logo, Examples and the bottle are below :) The bottle this label will go on it the "brimolantic" bottle below.

Please see the attached artwork.

Target Market(s)

Medical Practice

Industry/Entity Type

Supplement

Font styles to use
Serif
Sans Serif

Colors
33a6d7
0392cd
85cae6
7f7f7f
b2b2b2
9d9d9d
e8e8e8
d5d5d5

Requirements
Must have
• Clean simple

```html
<!DOCTYPE html>
<html lang="en">
<head>
<meta charset="utf-8">
<title>Brimolantic Dietary Supplement – Label Options</title>
<link rel="stylesheet" href="https://fonts.googleapis.com/css2?family=Oswald:wght@200;600&family=Raleway:wght@300&family=Open+Sans:wght@400&display=swap">
<style>
  :root {
    --blue-deep: #1a80b0;
    --blue-pale: #a9d3ef;
    --grey-dark: #7f7f7f;
    --grey-mid: #9d9d9d;
    --grey-light: #b2b2b2;
    --grey-rule: #d5d5d5;
    --grey-wash: #e8e8e8;
    --ink: #444444;
    --letter: #555555;
    --paper: #ffffff;
    --stage: #f7f7f7;
  }
  * { margin: 0; padding: 0; box-sizing: border-box; }
  html, body { width: 1200px; height: 1000px; overflow: hidden; }
  body {
    background: var(--stage);
    position: relative;
    font-family: "Open Sans", Arial, sans-serif;
    color: var(--grey-dark);
  }
  .label {
    position: absolute;
    top: 335px;
    width: 470px;
    height: 480px;
    background: var(--paper);
    border: 1px solid var(--grey-wash);
    overflow: hidden;
  }
  .label--c { left: 78px; }
  .label--d { left: 645px; }
  .abs { position: absolute; white-space: nowrap; }

  .divider {
    position: absolute;
    left: 594px; top: 130px;
    width: 8px; height: 740px;
    background: radial-gradient(circle, var(--grey-light) 3px, transparent 3.5px) 0 0 / 8px 29px repeat-y;
  }
  .option-letter {
    position: absolute;
    top: 870px;
    font-family: "Oswald", "Arial Narrow", sans-serif;
    font-weight: 600;
    font-size: 92px;
    line-height: 1;
    color: var(--letter);
  }

  .display {
    font-family: "Oswald", "Arial Narrow", sans-serif;
    font-weight: 200;
    line-height: 1;
  }
  .rule { height: 2px; background: var(--grey-rule); }

  .brand { display: flex; align-items: center; gap: 8px; }
  .brand-name {
    font-family: "Raleway", Arial, sans-serif; font-weight: 300;
    color: var(--grey-dark); letter-spacing: 0.5px; line-height: 1;
  }
  .brand-dot { border-radius: 50%; background: var(--blue-pale); flex: none; }

  .flavor-badge {
    display: flex; align-items: center; justify-content: center;
    border-radius: 50%; text-align: left; white-space: normal;
    color: var(--paper);
  }

  /* Option C */
  .c-bar { left: 4px; top: 5px; width: 38px; height: 470px; background: var(--blue-deep); }
  .c-title { left: 52px; top: 33px; width: 395px; font-size: 70px; letter-spacing: 5px; color: var(--blue-deep); }
  .c-sub { left: 54px; top: 104px; width: 395px; font-size: 50px; letter-spacing: 2.5px; color: var(--grey-dark); }
  .c-rule-top { left: 55px; top: 165px; width: 392px; }
  .c-tagline { left: 55px; top: 173px; font-size: 15.5px; color: var(--grey-dark); }
  .c-band {
    left: 57px; top: 213px; width: 392px; height: 32px;
    background: var(--blue-deep); color: var(--paper);
    font-size: 19px; line-height: 32px; padding-left: 9px; letter-spacing: 0.3px;
  }
  .c-rule-logo-a { left: 59px; top: 292px; width: 206px; }
  .c-rule-logo-b { left: 59px; top: 403px; width: 206px; }
  .c-brand { left: 62px; top: 334px; }
  .c-brand .brand-name { font-size: 22px; }
  .c-brand .brand-dot { width: 22px; height: 22px; }
  .c-badge {
    left: 277px; top: 265px; width: 154px; height: 154px;
    background: var(--blue-deep);
    box-shadow: 0 0 0 3px var(--paper), 0 0 0 9px var(--blue-deep);
    border: 5px dotted var(--paper);
    font-size: 20px; line-height: 1.1;
  }
  .c-netwt { left: 55px; top: 430px; font-size: 14px; color: var(--ink); }

  /* Option D */
  .d-title, .d-sub {
    transform: rotate(-90deg); transform-origin: top left;
    color: var(--grey-mid); text-align: center; width: 435px;
  }
  .d-title { left: 15px; top: 455px; font-size: 70px; line-height: 70px; letter-spacing: 11px; }
  .d-sub { left: 100px; top: 455px; font-size: 48px; line-height: 50px; letter-spacing: 3px; }
  .d-bar { left: 152px; top: 15px; width: 9px; height: 435px; background: var(--blue-pale); }
  .d-brand { left: 178px; top: 82px; }
  .d-brand .brand-name { font-size: 28px; }
  .d-brand .brand-dot { width: 34px; height: 34px; }
  .d-rule-top { left: 175px; top: 158px; width: 280px; }
  .d-tagline { left: 175px; top: 166px; font-size: 18px; line-height: 1.2; color: var(--grey-dark); }
  .d-band {
    left: 175px; top: 230px; width: 283px; height: 21px;
    background: var(--grey-dark); color: var(--paper);
    font-size: 14px; line-height: 21px; padding-left: 6px;
  }
  .d-badge {
    left: 298px; top: 288px; width: 134px; height: 134px;
    background: var(--blue-pale);
    box-shadow: 0 0 0 3px var(--paper), 0 0 0 8px var(--blue-pale);
    border: 4px dotted var(--paper);
    font-size: 18px; line-height: 1.15;
  }
  .d-netwt { left: 220px; top: 442px; font-size: 14px; color: var(--ink); }
</style>
</head>
<body>

<section class="label label--c">
  <div class="abs c-bar"></div>
  <h1 class="abs display c-title">BRIMOLANTIC</h1>
  <p class="abs display c-sub">DIETARY SUPPLMENT</p>
  <div class="abs rule c-rule-top"></div>
  <p class="abs c-tagline">The Ultimate Powdered Multi for the Whole Family</p>
  <p class="abs c-band">FOR PROFESSIONAL USE ONLY</p>
  <div class="abs rule c-rule-logo-a"></div>
  <div class="abs brand c-brand"><span class="brand-name">LARKFIELD 31</span><span class="brand-dot"></span></div>
  <div class="abs rule c-rule-logo-b"></div>
  <div class="abs flavor-badge c-badge"><span>Natural<br>Fruit Punch<br>Flavor</span></div>
  <p class="abs c-netwt">NET WT. 240 G&nbsp; (8.5 OZ)</p>
</section>

<div class="divider"></div>

<section class="label label--d">
  <h1 class="abs display d-title">BRIMOLANTIC</h1>
  <p class="abs display d-sub">DIETARY SUPPLMENT</p>
  <div class="abs d-bar"></div>
  <div class="abs brand d-brand"><span class="brand-name">LARKFIELD 31</span><span class="brand-dot"></span></div>
  <div class="abs rule d-rule-top"></div>
  <p class="abs d-tagline">The Ultimate Powdered Multi<br>for the Whole Family</p>
  <p class="abs d-band">FOR PROFESSIONAL USE ONLY</p>
  <div class="abs flavor-badge d-badge"><span>Natural<br>Fruit Punch<br>Flavor</span></div>
  <p class="abs d-netwt">NET WT. 240 G&nbsp; (8.5 OZ)</p>
</section>

<span class="option-letter" style="left:290px;">C</span>
<span class="option-letter" style="left:876px;">D</span>

</body>
</html>
```